#LanternKiteBay - One man's journey to becoming a corporate escapee and how you can do it too!

A book that describes my journey from avoiding spy allegations in Abu Dhabi, drinking vodka with Senators in Moscow, avoiding TVR and Mafia in Uzbekistan, being shot at in Jakarta, evacuated out of riots in Ranchi India and evading custody in Beijing. It is how the importance of life was realised and the opportunity break out and disrupt the boring old politically driven large corporates by developing new platforms on the internet to provide better and cheaper new products and services.

```html
<!DOCTYPE html>
<html lang="en">
<head>
<meta charset="utf-8">
<title>Lantern Kite Bay – Book Cover</title>
<link rel="stylesheet" href="https://fonts.googleapis.com/css2?family=Bebas+Neue&family=Dosis:wght@600&family=Josefin+Sans:wght@400&display=swap">
<style>
  :root {
    --backdrop: #2b2b2b;
    --cover: #ffffff;
    --author: #f29a1f;
    --title: #111111;
    --subtitle: #1a1a1a;
    --glass-light: #f7f7f7;
    --glass-mid: #dcdcdc;
    --glass-dark: #9a9a9a;
  }
  * { margin: 0; padding: 0; box-sizing: border-box; }
  html, body {
    width: 973px;
    height: 1200px;
    overflow: hidden;
    background: var(--backdrop);
  }
  .book-cover {
    position: absolute;
    left: 146px;
    top: 120px;
    width: 680px;
    height: 960px;
    background: var(--cover);
    text-align: center;
  }
  .author {
    position: absolute;
    top: 66px;
    left: 0;
    width: 100%;
    font-family: "Dosis", sans-serif;
    font-weight: 600;
    font-size: 50px;
    letter-spacing: 1px;
    color: var(--author);
    text-transform: uppercase;
  }
  .title {
    position: absolute;
    top: 196px;
    left: 0;
    width: 100%;
    font-family: "Bebas Neue", sans-serif;
    font-weight: 400;
    font-size: 150px;
    line-height: 120px;
    letter-spacing: 2px;
    color: var(--title);
  }
  .title span { display: block; }
  .subtitle {
    position: absolute;
    top: 550px;
    left: 0;
    width: 100%;
    font-family: "Josefin Sans", sans-serif;
    font-weight: 400;
    font-size: 28px;
    letter-spacing: 0.5px;
    color: var(--subtitle);
    text-transform: uppercase;
  }
  .cover-image {
    position: absolute;
    left: 0;
    bottom: 70px;
    width: 100%;
    height: 250px;
    background:
      radial-gradient(ellipse 45% 35% at 45% 55%, var(--glass-dark) 0%, var(--glass-mid) 45%, transparent 100%),
      linear-gradient(180deg, var(--cover) 0%, var(--glass-light) 60%, var(--cover) 100%);
  }
</style>
</head>
<body>
  <main class="book-cover">
    <p class="author">Martin O. Hale</p>
    <h1 class="title"><span>Lantern</span><span>Kite</span><span>Bay</span></h1>
    <p class="subtitle">Step away from the desk</p>
    <div class="cover-image" role="img" aria-label="Broken wine glasses lying shattered on a white reflective surface"></div>
  </main>
</body>
</html>
```